Bright Path Therapies business cards and stationary

Need business cards and stationary designed to match previously made logo for for a new company based in Sydney NSW called 'Bright Path Therapies'.

We provide early intervention services and diagnostic assessment for children with disability and their families. I would like designs that are colourful and child friendly - possibly using feet/footprints/steps on a white background. The final design should communicate that we are family friendly, accepting and fun to work with.

Target Market(s)

Parents and Families
Teachers
Allied Health Professionals

Industry/Entity Type

Psychology

Contact Information for Business Card

Bright Path Therapies
www.brightpaththerapies.example
info@brightpaththerapies.example

Font styles to use
Sans Serif
Decorative
Script

Requirements
Must have
• Match the font and colour scheme of logo, along with footprint picture
Nice to have
• Clean and simple, while reflecting that I am working with families.
• Also- editable for when we make staff specific cards.

```html
<!DOCTYPE html>
<html lang="en">
<head>
<meta charset="utf-8">
<title>Bright Path Therapies – Business Card</title>
<link href="https://fonts.googleapis.com/css2?family=Roboto:wght@400;500;700&display=swap" rel="stylesheet">
<style>
  :root{
    --page:#e9e6e2;
    --card:#ffffff;
    --brand-red:#d6312f;
    --brand-blue:#2a5fa9;
    --ink:#2e2e2e;
    --foot-red:#e8403b;
    --foot-blue:#2d6fb0;
    --foot-orange:#f29a2e;
    --foot-green:#5fbb46;
  }
  html,body{margin:0;padding:0;width:1200px;height:969px;overflow:hidden;background:var(--page);}
  .card{
    position:absolute;left:100px;top:201px;width:1000px;height:567px;
    background:var(--card);border-radius:34px;overflow:hidden;
    box-shadow:0 10px 40px rgba(0,0,0,.12);
    font-family:"Roboto",Arial,sans-serif;color:var(--ink);
  }
  .footprints{position:absolute;left:0;top:0;width:1000px;height:567px;}
  .brand{
    position:absolute;right:54px;top:82px;display:flex;align-items:center;gap:18px;
  }
  .brand-mark{width:64px;height:64px;border-radius:50%;background:var(--brand-red);}
  .brand-name{font-size:40px;font-weight:500;color:var(--brand-blue);letter-spacing:.5px;white-space:nowrap;}
  .person{position:absolute;right:54px;top:206px;text-align:right;}
  .person-name{font-size:30px;font-weight:700;color:var(--brand-red);margin:0;line-height:1.1;}
  .person-role{font-size:23px;font-weight:500;color:var(--brand-blue);margin:6px 0 0;}
  .address{position:absolute;right:54px;top:296px;text-align:right;font-size:22px;line-height:31px;margin:0;font-style:normal;}
  .contacts{position:absolute;right:54px;top:377px;list-style:none;margin:0;padding:0;font-size:22px;}
  .contacts li{display:flex;justify-content:flex-end;align-items:center;gap:14px;height:31.5px;}
  .contacts svg{width:20px;height:20px;fill:var(--brand-red);flex:none;}
</style>
</head>
<body>
<div class="card">
  <svg class="footprints" viewBox="0 0 1000 567">
    <defs>
      <radialGradient id="g-red"><stop offset="0" stop-color="var(--foot-red)"/><stop offset="1" stop-color="var(--foot-red)" stop-opacity=".75"/></radialGradient>
      <radialGradient id="g-blue"><stop offset="0" stop-color="var(--foot-blue)"/><stop offset="1" stop-color="var(--foot-blue)" stop-opacity=".75"/></radialGradient>
      <radialGradient id="g-orange"><stop offset="0" stop-color="var(--foot-orange)"/><stop offset="1" stop-color="var(--foot-orange)" stop-opacity=".75"/></radialGradient>
      <radialGradient id="g-green"><stop offset="0" stop-color="var(--foot-green)"/><stop offset="1" stop-color="var(--foot-green)" stop-opacity=".75"/></radialGradient>
    </defs>
    <ellipse role="img" aria-label="Red footprint illustration" cx="70" cy="200" rx="120" ry="85" fill="url(#g-red)"/>
    <ellipse role="img" aria-label="Blue footprint illustration" cx="60" cy="440" rx="100" ry="88" fill="url(#g-blue)"/>
    <ellipse role="img" aria-label="Orange footprint illustration" cx="198" cy="475" rx="78" ry="88" fill="url(#g-orange)"/>
    <ellipse role="img" aria-label="Green footprint illustration" cx="396" cy="475" rx="86" ry="100" fill="url(#g-green)"/>
  </svg>

  <div class="brand">
    <span class="brand-mark"></span>
    <span class="brand-name">Bright Path Therapies</span>
  </div>

  <div class="person">
    <p class="person-name">MAYA TURNER</p>
    <p class="person-role">CEO/FOUNDER</p>
  </div>

  <address class="address">42 Wattle Grove Road<br>Kellyton, NSW 2199</address>

  <ul class="contacts">
    <li>555 301 7720
      <svg viewBox="0 0 24 24"><path d="M6.6 10.8a15.1 15.1 0 0 0 6.6 6.6l2.2-2.2a1 1 0 0 1 1-.25 11.4 11.4 0 0 0 3.6.57 1 1 0 0 1 1 1V20a1 1 0 0 1-1 1A17 17 0 0 1 3 4a1 1 0 0 1 1-1h3.5a1 1 0 0 1 1 1c0 1.25.2 2.45.57 3.57a1 1 0 0 1-.25 1z"/></svg></li>
    <li>555 482 6615
      <svg viewBox="0 0 24 24"><path d="M7 1h10a2 2 0 0 1 2 2v18a2 2 0 0 1-2 2H7a2 2 0 0 1-2-2V3a2 2 0 0 1 2-2zm0 3v14h10V4zm5 15.5a1.2 1.2 0 1 0 0 2.4 1.2 1.2 0 0 0 0-2.4z"/></svg></li>
    <li>555 237 0846
      <svg viewBox="0 0 24 24"><path d="M6 2h12v5H6zM3 8h18a2 2 0 0 1 2 2v7h-4v5H5v-5H1v-7a2 2 0 0 1 2-2zm4 8v4h10v-4z"/></svg></li>
    <li>info@brightpaththerapies.example
      <svg viewBox="0 0 24 24"><path d="M2 5h20v14H2zm2 2v.5l8 5 8-5V7zm0 2.8V17h16V9.8l-8 5z"/></svg></li>
    <li>www.brightpaththerapies.example
      <svg viewBox="0 0 24 24"><path d="M12 2a10 10 0 1 0 0 20 10 10 0 0 0 0-20zm6.9 6h-3a15 15 0 0 0-1.3-3.9A8 8 0 0 1 18.9 8zM12 4c.8 1.1 1.5 2.5 1.9 4h-3.8c.4-1.5 1.1-2.9 1.9-4zM4.3 14a8 8 0 0 1 0-4h3.4a16 16 0 0 0 0 4zm.8 2h3a15 15 0 0 0 1.3 3.9A8 8 0 0 1 5.1 16zm3-8h-3a8 8 0 0 1 4.3-3.9A15 15 0 0 0 8.1 8zM12 20c-.8-1.1-1.5-2.5-1.9-4h3.8c-.4 1.5-1.1 2.9-1.9 4zm2.3-6H9.7a14 14 0 0 1 0-4h4.6a14 14 0 0 1 0 4zm.3 5.9a15 15 0 0 0 1.3-3.9h3a8 8 0 0 1-4.3 3.9zm1.7-5.9a16 16 0 0 0 0-4h3.4a8 8 0 0 1 0 4z"/></svg></li>
  </ul>
</div>
</body>
</html>
```